" Empresa de desenvolvimento humano, que trabalha principalmente a gestão dentro do ambiente de trabalho através de treinamento, consultoria e coaching. O principal conceito é que cada pessoa é única e seu auto-conhecimento é a chave para seu sucesso. "

```html
<!DOCTYPE html>
<html lang="pt-BR">
<head>
<meta charset="UTF-8">
<title>Integra — Resultados trimestrais</title>
<link rel="stylesheet" href="https://fonts.googleapis.com/css2?family=Montserrat:wght@700&family=Open+Sans:wght@400&display=swap">
<style>
  :root {
    --page: #ffffff;
    --wave-light: #2a7fa8;
    --wave-dark: #0b3049;
    --wave-edge: #4d5358;
    --title: #3b6f92;
    --bar-front: #5b9bd5;
    --bar-side: #3f78ad;
    --bar-top: #8ab8e4;
    --grid: #d9d9d9;
    --label: #595959;
    --pie-blue: #5b9bd5;
    --pie-blue-side: #3a6d9e;
    --pie-orange: #ed7d31;
    --pie-orange-side: #b55c1f;
    --pie-grey: #a5a5a5;
    --pie-yellow: #ffc000;
    --brand: #1f4e6e;
  }
  html, body {
    margin: 0;
    width: 1200px;
    height: 1200px;
    overflow: hidden;
    background: var(--page);
  }
  .slide {
    position: relative;
    width: 1200px;
    height: 1200px;
    font-family: "Open Sans", Arial, sans-serif;
  }
  .slide svg { position: absolute; inset: 0; }
  .chart-title {
    font-family: "Montserrat", Arial, sans-serif;
    font-weight: 700;
    font-size: 30px;
    fill: var(--title);
    letter-spacing: 1px;
  }
  .axis-label, .legend-label {
    font-size: 13px;
    fill: var(--label);
  }
  .brand-name {
    position: absolute;
    left: 1000px;
    top: 890px;
    display: flex;
    align-items: center;
    gap: 10px;
    font-family: "Montserrat", Arial, sans-serif;
    font-weight: 700;
    font-size: 30px;
    letter-spacing: 2px;
    color: var(--brand);
  }
  .brand-dot {
    width: 22px;
    height: 22px;
    border-radius: 50%;
    background: var(--brand);
  }
</style>
</head>
<body>
<main class="slide">
  <svg width="1200" height="1200" viewBox="0 0 1200 1200">
    <defs>
      <linearGradient id="wave-fill" x1="0" y1="0" x2="1" y2="0">
        <stop offset="0" stop-color="var(--wave-light)"/>
        <stop offset="1" stop-color="var(--wave-dark)"/>
      </linearGradient>
    </defs>

    <!-- side wave -->
    <g class="side-wave">
      <path d="M0 240 L185 240 C150 330 160 420 240 560 C290 650 260 800 175 948 L0 948 Z" fill="url(#wave-fill)"/>
      <path d="M185 240 C150 330 160 420 240 560 C290 650 260 800 175 948" fill="none" stroke="var(--wave-edge)" stroke-width="10"/>
    </g>

    <!-- pie chart -->
    <g class="pie-chart">
      <text class="chart-title" x="907" y="312" text-anchor="middle">TITULO 2</text>
      <path d="M1135 444 A228 108 0 0 1 789.6 536.6 L789.6 572.6 A228 108 0 0 0 1135 480 Z" fill="var(--pie-blue-side)"/>
      <path d="M789.6 536.6 A228 108 0 0 1 679 444 L679 480 A228 108 0 0 0 789.6 572.6 Z" fill="var(--pie-orange-side)"/>
      <path d="M907 444 L907 336 A228 108 0 1 1 789.6 536.6 Z" fill="var(--pie-blue)"/>
      <path d="M907 444 L789.6 536.6 A228 108 0 0 1 697.7 401.1 Z" fill="var(--pie-orange)"/>
      <path d="M907 444 L697.7 401.1 A228 108 0 0 1 791 351 Z" fill="var(--pie-grey)"/>
      <path d="M907 444 L791 351 A228 108 0 0 1 907 336 Z" fill="var(--pie-yellow)"/>
      <g class="pie-legend">
        <circle cx="808" cy="622" r="4" fill="var(--pie-blue)"/><text class="legend-label" x="816" y="627">1º Tri</text>
        <circle cx="866" cy="622" r="4" fill="var(--pie-orange)"/><text class="legend-label" x="874" y="627">2º Tri</text>
        <circle cx="924" cy="622" r="4" fill="var(--pie-grey)"/><text class="legend-label" x="932" y="627">3º Tri</text>
        <circle cx="982" cy="622" r="4" fill="var(--pie-yellow)"/><text class="legend-label" x="990" y="627">4º Tri</text>
      </g>
    </g>

    <!-- bar chart -->
    <g class="bar-chart">
      <text class="chart-title" x="504" y="552" text-anchor="middle">TITULO 2</text>
      <g class="grid" stroke="var(--grid)" stroke-width="1.5">
        <line x1="300" y1="792" x2="720" y2="850"/>
        <line x1="300" y1="772" x2="720" y2="830"/>
        <line x1="300" y1="752" x2="720" y2="810"/>
        <line x1="300" y1="732" x2="720" y2="790"/>
        <line x1="300" y1="712" x2="720" y2="770"/>
        <line x1="300" y1="692" x2="720" y2="750"/>
        <line x1="300" y1="672" x2="720" y2="730"/>
        <line x1="300" y1="652" x2="720" y2="710"/>
        <line x1="300" y1="632" x2="720" y2="690"/>
        <line x1="300" y1="612" x2="720" y2="670"/>
        <line x1="300" y1="612" x2="300" y2="792"/>
      </g>
      <g class="axis-values" text-anchor="end">
        <text class="axis-label" x="290" y="797">0</text>
        <text class="axis-label" x="290" y="777">1</text>
        <text class="axis-label" x="290" y="757">2</text>
        <text class="axis-label" x="290" y="737">3</text>
        <text class="axis-label" x="290" y="717">4</text>
        <text class="axis-label" x="290" y="697">5</text>
        <text class="axis-label" x="290" y="677">6</text>
        <text class="axis-label" x="290" y="657">7</text>
        <text class="axis-label" x="290" y="637">8</text>
        <text class="axis-label" x="290" y="617">9</text>
      </g>
      <g class="bars">
        <path d="M336 619 L348 609 L386 609 L374 619 Z" fill="var(--bar-top)"/>
        <path d="M374 619 L386 609 L386 782 L374 792 Z" fill="var(--bar-side)"/>
        <rect x="336" y="619" width="38" height="173" fill="var(--bar-front)"/>

        <path d="M437 732 L449 722 L487 722 L475 732 Z" fill="var(--bar-top)"/>
        <path d="M475 732 L487 722 L487 799 L475 809 Z" fill="var(--bar-side)"/>
        <rect x="437" y="732" width="38" height="77" fill="var(--bar-front)"/>

        <path d="M533 782 L545 772 L583 772 L571 782 Z" fill="var(--bar-top)"/>
        <path d="M571 782 L583 772 L583 818 L571 828 Z" fill="var(--bar-side)"/>
        <rect x="533" y="782" width="38" height="46" fill="var(--bar-front)"/>

        <path d="M630 806 L642 796 L680 796 L668 806 Z" fill="var(--bar-top)"/>
        <path d="M668 806 L680 796 L680 835 L668 845 Z" fill="var(--bar-side)"/>
        <rect x="630" y="806" width="38" height="39" fill="var(--bar-front)"/>
      </g>
      <g class="categories" text-anchor="middle">
        <text class="axis-label" x="350" y="832">1º Tri</text>
        <text class="axis-label" x="448" y="856">2º Tri</text>
        <text class="axis-label" x="548" y="873">3º Tri</text>
        <text class="axis-label" x="648" y="897">4º Tri</text>
      </g>
      <g class="bar-legend">
        <circle cx="482" cy="920" r="4" fill="var(--bar-front)"/>
        <text class="legend-label" x="490" y="925">Vendas</text>
      </g>
    </g>
  </svg>

  <div class="brand-name"><span class="brand-dot"></span>INTEGRA</div>
</main>
</body>
</html>
```